Catalogue Design Project

Hi all,

I would like to design Catalogue for our Range Hood products. I am looking for help to design a elegant catalogue impress our potential customer.

Thanks,

Brent

Target Market(s)

Our customers are in US, Canada as well as Australia.

Requirements
Must have
• Please used the pictures of range hood models from the attached file (6 models.rar). Our company information.

Nice to have
• It is nice if the cataloge design as a book style.

```html
<!DOCTYPE html>
<html lang="en">
<head>
<meta charset="utf-8">
<title>Northline Hood Works — Range Hood Catalogue 2013-14</title>
<link rel="stylesheet" href="https://fonts.googleapis.com/css2?family=Source+Sans+3:ital,wght@0,400;0,600;0,700;1,400&display=swap">
<style>
  :root {
    --bg: #d9d9d9;
    --navy: #0b1528;
    --brand-blue: #1ea6e0;
    --muted: #b9c0cc;
    --rule: #3a4760;
    --red: #d2232a;
    --orange: #ef6a23;
    --yellow: #f7c600;
    --yellow-deep: #f2a413;
    --green: #86bb1d;
    --green-light: #c9de2a;
    --lime-pale: #e4ef7c;
    --steel-light: #e6e8ea;
    --steel-dark: #8c9196;
    --ink: #1d1d1b;
    --ink-soft: #4a4a3a;
  }
  * { box-sizing: border-box; margin: 0; padding: 0; }
  html, body { width: 1200px; height: 1000px; overflow: hidden; }
  body {
    background: var(--bg);
    font-family: "Source Sans 3", "Myriad Pro", sans-serif;
    position: relative;
  }
  .page {
    position: absolute;
    width: 370px;
    height: 370px;
    overflow: hidden;
  }
  .product-photo {
    position: absolute;
    background: linear-gradient(180deg, var(--steel-light) 0%, #c4c8cc 55%, var(--steel-dark) 100%);
    border-radius: 2px;
  }
  .fold-line { position: absolute; top: 0; bottom: 0; width: 1px; }

  /* Cover */
  .cover { left: 30px; top: 315px; background: var(--navy); }
  .cover .fold-line { left: 200px; background: var(--rule); }
  .brand-block {
    position: absolute; left: 212px; top: 96px;
    display: flex; flex-direction: column; align-items: flex-start;
  }
  .brand-mark { width: 22px; height: 22px; background: var(--brand-blue); margin-bottom: 10px; }
  .brand-name {
    color: var(--brand-blue); font-weight: 700; font-size: 22px; line-height: 0.95;
    letter-spacing: 0.3px; text-transform: uppercase;
  }
  .brand-country { color: var(--brand-blue); font-size: 13px; line-height: 1.2; margin-top: 3px; }
  .brand-web { color: var(--muted); font-size: 8px; line-height: 1.4; }
  .edition {
    position: absolute; right: 180px; top: 196px;
    display: flex; flex-direction: column; align-items: flex-end; color: #e6e9ef;
  }
  .edition-year { font-size: 17px; font-weight: 600; line-height: 1.1; }
  .edition-title { font-size: 10px; color: var(--muted); line-height: 1.3; }
  .model-strip { position: absolute; left: 100px; top: 278px; display: flex; gap: 8px; }
  .model-tile { width: 60px; height: 60px; position: relative; }
  .model-tile .product-photo { left: 11px; top: 17px; width: 38px; height: 26px; }
  .tile-red { background: var(--red); }
  .tile-orange { background: var(--orange); }
  .tile-yellow { background: var(--yellow); }
  .tile-green { background: var(--green); }

  /* Spread */
  .page-left {
    left: 430px; top: 315px;
    background: linear-gradient(180deg, var(--yellow) 0%, var(--yellow) 45%, var(--yellow-deep) 100%);
  }
  .page-right { left: 800px; top: 315px; background: var(--green); }
  .page-left .fold-line { left: 200px; background: rgba(255,255,255,0.45); }
  .page-right .fold-line { left: 170px; background: rgba(255,255,255,0.4); }
  .accent-circle { position: absolute; border-radius: 50%; }
  .page-left .accent-circle { left: -40px; top: 150px; width: 300px; height: 300px; background: rgba(240,140,20,0.35); }
  .page-right .circle-large { left: 180px; top: -20px; width: 260px; height: 260px; background: var(--green-light); }
  .page-right .circle-small { left: 280px; top: -30px; width: 140px; height: 140px; background: var(--lime-pale); opacity: .8; }

  .spec-list { position: absolute; list-style: none; font-size: 10.5px; line-height: 1.7; color: var(--ink); }
  .spec-list b { font-weight: 700; }
  .page-left .spec-list { left: 214px; top: 96px; }
  .page-right .spec-list { left: 182px; top: 268px; color: var(--ink-soft); font-size: 10px; }
  .feature-note {
    position: absolute; left: 18px; top: 270px; list-style: none;
    font-size: 6px; line-height: 1.5; color: var(--ink-soft);
  }
  .feature-note .note-title { font-style: italic; }
</style>
</head>
<body>

  <section class="page cover" aria-label="Catalogue cover">
    <div class="fold-line"></div>
    <div class="brand-block">
      <span class="brand-mark"></span>
      <span class="brand-name">Northline<br>Hood<br>Works</span>
      <span class="brand-country">Vietnam</span>
      <span class="brand-web">www.northlinehood.com</span>
    </div>
    <div class="edition">
      <span class="edition-year">2013-14</span>
      <span class="edition-title">Range hood products</span>
    </div>
    <div class="model-strip">
      <div class="model-tile tile-red"><div class="product-photo" role="img" aria-label="Chimney range hood model"></div></div>
      <div class="model-tile tile-orange"><div class="product-photo" role="img" aria-label="Angled glass range hood model"></div></div>
      <div class="model-tile tile-yellow"><div class="product-photo" role="img" aria-label="Under-cabinet range hood model"></div></div>
      <div class="model-tile tile-green"><div class="product-photo" role="img" aria-label="Slim range hood model"></div></div>
    </div>
  </section>

  <section class="page page-left" aria-label="Catalogue page: touch control model">
    <div class="accent-circle"></div>
    <div class="fold-line"></div>
    <div class="product-photo" role="img" aria-label="Small view of stainless under-cabinet range hood" style="left:218px;top:40px;width:92px;height:40px;"></div>
    <ul class="spec-list">
      <li><b>Control:</b> Cap. Touch 3 speed</li>
      <li><b>Display:</b> LED indicates</li>
      <li><b>Gross weight:</b> 11 kg</li>
      <li><b>Dimension:</b> 755x255x250 mm</li>
    </ul>
    <div class="product-photo" role="img" aria-label="Large stainless range hood with touch control panel" style="left:-10px;top:200px;width:250px;height:120px;"></div>
  </section>

  <section class="page page-right" aria-label="Catalogue page: push button model">
    <div class="accent-circle circle-large"></div>
    <div class="accent-circle circle-small"></div>
    <div class="fold-line"></div>
    <div class="product-photo" role="img" aria-label="Large stainless range hood with push button panel" style="left:-10px;top:20px;width:290px;height:120px;"></div>
    <div class="product-photo" role="img" aria-label="Small view of stainless under-cabinet range hood" style="left:200px;top:220px;width:80px;height:36px;"></div>
    <ul class="spec-list">
      <li>Control: Push Button 3 speed</li>
      <li>Display: LCD Screen</li>
      <li>Gross weight: 11 kg</li>
      <li>Dimension: 755x255x250 mm</li>
    </ul>
    <ul class="feature-note">
      <li class="note-title">Optional features</li>
      <li>• Auto shut-off • Dual lights</li>
      <li>• Baffle filters • Quiet motor</li>
    </ul>
  </section>

</body>
</html>
```